Please use the logo / design elements and font to design a business card that is eye catching and informative. If using "Direct Primary Care" logo element, you don't have to spell it out in the text.

Dr. Marcus Pellam
Vale Wellness - Direct Primary Care
4817 Tindell Rd. Suite 305
Brennock, AR 72990
Phone: 555-318-7240
ValeWellnessAR.example

```html
<!DOCTYPE html>
<html lang="en">
<head>
<meta charset="utf-8">
<title>Vale Wellness – Business Card</title>
<link rel="stylesheet" href="https://fonts.googleapis.com/css2?family=Poppins:wght@500;700&family=Montserrat:wght@400;500&display=swap">
<style>
  :root {
    --stage: #2b2b2e;
    --navy: #0a1633;
    --ink: #0f1a3c;
    --blue: #3a5fb0;
    --sky: #3fb3e6;
    --paper: #ffffff;
    --text: #1c1c1f;
  }
  * { margin: 0; padding: 0; box-sizing: border-box; }
  html, body { width: 1200px; height: 875px; overflow: hidden; }
  body {
    background: var(--stage);
    display: flex;
    flex-direction: column;
    align-items: center;
    justify-content: center;
    gap: 40px;
  }
  .card {
    position: relative;
    width: 640px;
    height: 366px;
    border-radius: 22px;
    overflow: hidden;
    box-shadow: 0 18px 40px rgba(0,0,0,.45);
  }
  .card--front {
    background: var(--navy);
    display: flex;
    align-items: center;
    justify-content: center;
    gap: 22px;
  }
  .front-brand__dot {
    width: 54px; height: 54px; border-radius: 50%;
    background: var(--sky);
  }
  .front-brand__name {
    font-family: "Poppins", sans-serif;
    font-weight: 500;
    font-size: 66px;
    color: var(--paper);
    letter-spacing: -1px;
  }
  .card--back { background: var(--paper); }
  .back-brand {
    position: absolute; left: 44px; top: 76px;
    display: flex; align-items: center; gap: 10px;
  }
  .back-brand__dot { width: 22px; height: 22px; border-radius: 50%; background: var(--blue); }
  .back-brand__name {
    font-family: "Poppins", sans-serif;
    font-weight: 500;
    font-size: 34px;
    color: var(--ink);
    letter-spacing: -.5px;
  }
  .holder {
    position: absolute; right: 44px; top: 40px; text-align: right;
  }
  .holder__name {
    font-family: "Poppins", sans-serif; font-weight: 700;
    font-size: 24px; color: var(--ink);
  }
  .holder__role {
    font-family: "Montserrat", sans-serif; font-weight: 500;
    font-size: 12.5px; color: var(--text); margin-top: 2px;
  }
  .contact {
    position: absolute; left: 44px; bottom: 40px;
    font-family: "Montserrat", sans-serif; font-size: 14px;
    color: var(--text); line-height: 1.45;
  }
  .contact__address { margin-bottom: 10px; }
  .contact__row { display: flex; align-items: center; gap: 10px; }
  .contact__row svg { width: 15px; height: 15px; flex: none; }
</style>
</head>
<body>
  <section class="card card--front">
    <div class="front-brand__dot"></div>
    <div class="front-brand__name">Vale Wellness</div>
  </section>

  <section class="card card--back">
    <div class="back-brand">
      <div class="back-brand__dot"></div>
      <div class="back-brand__name">Vale Wellness</div>
    </div>

    <div class="holder">
      <div class="holder__name">Dr. Marcus Pellam</div>
      <div class="holder__role">Vale Wellness - Direct Primary Care</div>
    </div>

    <div class="contact">
      <div class="contact__address">4817 Tindell Rd. Suite 305<br>Brennock, AR 72990</div>
      <div class="contact__row">
        <svg viewBox="0 0 24 24" aria-hidden="true"><path fill="#3a5fb0" d="M6.6 10.8a15 15 0 0 0 6.6 6.6l2.2-2.2a1 1 0 0 1 1-.25 11.4 11.4 0 0 0 3.6.57 1 1 0 0 1 1 1V20a1 1 0 0 1-1 1A17 17 0 0 1 3 4a1 1 0 0 1 1-1h3.5a1 1 0 0 1 1 1c0 1.25.2 2.45.57 3.57a1 1 0 0 1-.25 1z"/></svg>
        <span>555-318-7240</span>
      </div>
      <div class="contact__row">
        <svg viewBox="0 0 24 24" aria-hidden="true"><rect x="2" y="5" width="20" height="14" rx="2" fill="#3fb3e6"/><path d="M3 6l9 7 9-7" stroke="#fff" stroke-width="1.6" fill="none"/></svg>
        <span>www.ValeWellnessAR.example</span>
      </div>
    </div>
  </section>
</body>
</html>
```